Business Card Design Project

Company name KD MOTOR SERVICES
KD MOTOR
name of owner: Dorvan Pleth
Phone: 604-555-0187
Email: info@kdmotor-example.ca
website: www.kdmotor-example.info
Address
48217 19 Ave Surrey, BC V0X 9Z4

Black Back round

Industry/Entity Type

Business

```html
<!DOCTYPE html>
<html lang="en">
<head>
<meta charset="utf-8">
<title>KD Motor Services – Business Card</title>
<link rel="stylesheet" href="https://fonts.googleapis.com/css2?family=Arimo:wght@400;700&display=swap">
<style>
  :root {
    --page: #d9d9d9;
    --card: #0c0d12;
    --card-edge: #16171d;
    --ink: #ffffff;
    --ink-soft: #b9bcc4;
    --rule: #8a8d95;
  }
  * { box-sizing: border-box; margin: 0; padding: 0; }
  html, body { width: 1200px; height: 1200px; overflow: hidden; }
  body {
    background: var(--page);
    font-family: "Arimo", Arial, sans-serif;
    color: var(--ink);
    display: flex;
    flex-direction: column;
    align-items: center;
    justify-content: center;
    gap: 60px;
  }
  .card {
    position: relative;
    width: 840px;
    height: 480px;
    background: radial-gradient(ellipse at 60% 40%, var(--card-edge), var(--card) 70%);
    overflow: hidden;
    box-shadow: 0 6px 18px rgba(0,0,0,.25);
  }

  /* Front */
  .car-photo {
    position: absolute;
    left: 0; top: 0;
    width: 520px; height: 480px;
    background:
      radial-gradient(ellipse 70% 22% at 45% 52%, #3a3c44 0%, #1d1e24 55%, transparent 80%),
      linear-gradient(180deg, var(--card) 0%, var(--card) 62%, #5e6068 78%, #e6e6e8 100%);
  }
  .front-brand {
    position: absolute;
    right: 110px; top: 200px;
    text-align: right;
  }
  .front-brand .company {
    font-size: 26px;
    font-weight: 400;
    letter-spacing: 0.5px;
  }
  .front-brand .web {
    margin-top: 8px;
    font-size: 14px;
    color: var(--ink-soft);
  }
  .front-pointer { position: absolute; right: 0; top: 215px; }

  /* Back */
  .back-pointer { position: absolute; left: 0; top: 40px; }
  .owner { position: absolute; left: 100px; top: 42px; }
  .owner .name { font-size: 20px; }
  .owner .role { font-size: 13px; color: var(--ink-soft); margin-top: 4px; }
  .back-company {
    position: absolute;
    left: 60px; top: 205px;
    font-size: 26px;
    letter-spacing: 0.5px;
  }
  .contacts {
    position: absolute;
    left: 430px; top: 240px;
    border-left: 1px solid var(--rule);
    list-style: none;
  }
  .contacts li {
    display: flex;
    align-items: center;
    gap: 16px;
    height: 34px;
    margin-left: -9px;
    font-size: 16px;
  }
  .contacts svg { width: 18px; height: 18px; background: var(--card); padding: 2px; }
</style>
</head>
<body>

<section class="card card-front">
  <div class="car-photo" role="img" aria-label="Photograph of a black sports car in side view on a light studio floor"></div>
  <div class="front-brand">
    <div class="company">KD MOTOR SERVICES</div>
    <div class="web">www.kdmotor-example.info</div>
  </div>
  <svg class="front-pointer" width="44" height="60" viewBox="0 0 44 60" aria-hidden="true">
    <polygon points="44,0 44,60 0,30" fill="#fff"/>
  </svg>
</section>

<section class="card card-back">
  <svg class="back-pointer" width="44" height="60" viewBox="0 0 44 60" aria-hidden="true">
    <polygon points="0,0 44,30 0,60" fill="#fff"/>
  </svg>
  <div class="owner">
    <div class="name">Dorvan Pleth</div>
    <div class="role">Owner</div>
  </div>
  <div class="back-company">KD MOTOR SERVICES</div>
  <ul class="contacts">
    <li>
      <svg viewBox="0 0 24 24" aria-hidden="true"><path fill="#fff" d="M6.6 10.8a15 15 0 0 0 6.6 6.6l2.2-2.2c.3-.3.7-.4 1-.2 1.1.4 2.3.6 3.6.6.6 0 1 .4 1 1V20c0 .6-.4 1-1 1A17 17 0 0 1 3 4c0-.6.4-1 1-1h3.5c.6 0 1 .4 1 1 0 1.3.2 2.5.6 3.6.1.3 0 .7-.2 1z"/></svg>
      <span>604-555-0187</span>
    </li>
    <li>
      <svg viewBox="0 0 24 24" aria-hidden="true"><path fill="#fff" d="M2 5h20v14H2z"/><path fill="none" stroke="#0c0d12" stroke-width="1.8" d="M2 5l10 8 10-8"/></svg>
      <span>info@kdmotor-example.ca</span>
    </li>
    <li>
      <svg viewBox="0 0 24 24" aria-hidden="true"><circle cx="12" cy="12" r="9" fill="none" stroke="#fff" stroke-width="2"/><path fill="none" stroke="#fff" stroke-width="1.5" d="M3 12h18M12 3c3 3 3 15 0 18M12 3c-3 3-3 15 0 18"/></svg>
      <span>www.kdmotor-example.info</span>
    </li>
    <li>
      <svg viewBox="0 0 24 24" aria-hidden="true"><path fill="#fff" d="M12 2a7 7 0 0 0-7 7c0 5 7 13 7 13s7-8 7-13a7 7 0 0 0-7-7zm0 9.5A2.5 2.5 0 1 1 12 6.5a2.5 2.5 0 0 1 0 5z"/></svg>
      <span>48217 19 Ave Surrey, BC V0X 9Z4</span>
    </li>
  </ul>
</section>

</body>
</html>
```